Design eBook cover and interior pages for vegan investment consulting firm and membership service...

I have completed an eBook that is about 6 pages of printed text (see attached PDF). I am seeking a cover page and a cool design for the interior pages. The final product should be as concise as possible while being easy to read, and not to exceed 10 pages total in any case.

My business is named Plantwise Harbor. You can learn more about the company by visiting https://plantwiseharbor.example. There, you’ll also see our current color and design choices.

We are about to start a Phase II redesign of the website, so it is not required that you match the color and style of our website. I am open to any fresh ideas regarding color, fonts, and overall aesthetic that might also inform our website redesign.

The business serves individuals “investor members” who have $50,000 or more in their investment portfolio, and also provides “purpose driven” portfolio design consulting to endowments, large asset managers, and high net worth individuals who are looking to build a vegan portfolio over $10 million or more.

Because we’re dealing with investing and people’s life savings, we want the eBook look to convey responsibility and integrity. At the same time, our audience will participate because of they are also passionate about all things vegan - protecting animals, the environment, and human health. To summarize, the goal is to have an eBook design that conveys a blend of responsibility, integrity, and passion.

Note - there is a tendency for people to first think of the color green when designing for vegan enterprises. I feel that using green as a major and even as a minor color often creates difficult or weak design outcomes. Green has become a kind of design shorthand for all things vegan and environmental, and as a result, I feel it has lost any special meaning.

Since we provide serious services to people who take investing seriously, I want color and design styles that read well, and convey responsibility, integrity and passion without relying on overused design cliches, but while still conveying a fresh perspective.

```html
<!DOCTYPE html>
<html lang="en">
<head>
<meta charset="UTF-8">
<title>Plantwise Harbor — Leading Vegan Investment Opportunities Today</title>
<link rel="stylesheet" href="https://fonts.googleapis.com/css2?family=Roboto:wght@400&family=Open+Sans:wght@400&display=swap">
<style>
  :root {
    --accent: #9b0d1b;
    --rule: #7a2a30;
    --ink: #1f1f1f;
    --paper: #ffffff;
    --footer-rule: #8a8a8a;
  }
  * { margin: 0; padding: 0; box-sizing: border-box; }
  html, body { width: 927px; height: 1200px; overflow: hidden; background: var(--paper); }
  .page { position: relative; width: 927px; height: 1200px; background: var(--paper); }

  .page-title {
    position: absolute; left: 86px; top: 96px; width: 760px;
    font-family: "Roboto", sans-serif; font-weight: 400;
    font-size: 41px; line-height: 51px; color: var(--accent);
  }
  .title-rule {
    position: absolute; left: 86px; top: 207px; width: 755px;
    border-top: 1px solid var(--rule);
  }

  .content {
    position: absolute; left: 343px; top: 334px; width: 498px;
    font-family: "Open Sans", sans-serif; font-size: 14px; line-height: 26px;
    color: var(--ink); letter-spacing: 0.25px;
  }
  .content p { text-align: justify; text-indent: 26px; }
  .content p.lead-in, .content h2 + p { text-indent: 0; }
  .drop-cap {
    float: left; font-family: "Roboto", sans-serif; font-size: 76px;
    line-height: 62px; color: var(--accent); margin: 7px 6px 0 -2px;
  }
  .content h2 {
    font-family: "Roboto", sans-serif; font-weight: 400; font-size: 25px;
    line-height: 30px; color: var(--accent); margin: 48px 0 23px;
  }

  .page-footer {
    position: absolute; left: 86px; top: 1121px; width: 755px;
    border-top: 1px solid var(--footer-rule); padding-top: 6px;
    font-family: "Open Sans", sans-serif; font-size: 15px; letter-spacing: 0.4px;
    text-align: center; color: var(--ink);
  }
</style>
</head>
<body>
<main class="page">
  <h1 class="page-title">Leading Vegan Investment<br>Opportunities Today</h1>
  <div class="title-rule"></div>

  <article class="content">
    <p class="lead-in"><span class="drop-cap">T</span>wo major contributors to the growth of vegan products are existing demand by the large number of existing vegans, and the rapid, 1% annual growth in Americans identifying as vegans.</p>
    <p>Let’s look more closely at how this growth in vegan commitment is building businesses and creating investment opportunities in these five market segments.</p>

    <h2>1. Vegan Consumer Foods</h2>
    <p>Vegan substitutes for meat, dairy, and eggs are growing dramatically. New firms are entering the market at a rapid pace to satisfy the increase in demand for vegan packaged foods. This presents exceptional vegan investment opportunities as more people each year are increasingly turning to vegan products. U.S. sales of plant based dairy alternatives alone is already a $1.4 billion industry.</p>

    <h2>2. Vegan Restaurants</h2>
    <p>It is nearly impossible to find both a nutritious and fulfilling vegan meal at most fastfood restaurant chains. Yet, Vegans alone account for $67 billion of the total U.S. annual restaurant market.</p>
    <p>Sprout &amp; Ember, a vegan restaurant, serves approximately 40,000 customers a week, and their projected revenue for 2018 is $40 million.</p>
    <p>Emerging Vegan fast food brands like Sprout &amp; Ember and Greenleaf Quick Kitchen provide evidence that there is a massive demand for quick, vegan alternatives to major restaurant chains.</p>
  </article>

  <footer class="page-footer">5 VEGAN BUSINESSES YOU SHOULD BE INVESTING IN TODAY | Page 2</footer>
</main>
</body>
</html>
```